Larkmoor Health- Core Values Graphic for Visual Appeal

I would like a poster that could take these written core values from our organization and create a graphic that we could use for our staff and employees. I would also like to incorporate our branding into this project. Thank you!

Target Market(s)

To helps patients and employees understand the core values of our organization

Industry/Entity Type

Healthcare

Requirements
Must have
• Match our branding
Nice to have
• Please use your creativity!
Should not have
• Overly complex/ busy

```html
<!DOCTYPE html>
<html lang="en">
<head>
<meta charset="utf-8">
<title>Larkmoor Health – Core Values</title>
<link rel="stylesheet" href="https://fonts.googleapis.com/css2?family=Oswald:wght@300;400;500;600;700&family=Raleway:wght@400;500;600;700&display=swap">
<style>
  :root {
    --paper: #ebebeb;
    --ink: #454549;
    --blue: #2aa8e0;
    --blue-soft: #c6e0ec;
    --grey-shape: #dcdcdc;
    --numeral-blue: #d9e9f0;
    --numeral-grey: #d3d3d3;
    --art-fill: #d6e8f1;
    --orange: #f5a81c;
    --white: #ffffff;
  }
  * { margin: 0; padding: 0; box-sizing: border-box; }
  html, body { width: 849px; height: 1200px; overflow: hidden; background: var(--paper); }
  .poster {
    position: relative; width: 849px; height: 1200px; overflow: hidden;
    background: var(--paper); font-family: "Raleway", sans-serif; color: var(--ink);
  }
  .backdrop { position: absolute; inset: 0; }
  .numeral {
    position: absolute; font-family: "Oswald", sans-serif; font-weight: 700;
    font-size: 270px; line-height: 1;
  }
  .numeral--one { left: 14px; top: 360px; color: var(--numeral-blue); }
  .numeral--two { left: 664px; top: 494px; color: var(--numeral-grey); }
  .numeral--three { left: 34px; top: 664px; color: var(--numeral-grey); }
  .numeral--four { left: 700px; top: 828px; color: var(--numeral-grey); }

  .anatomy-art { position: absolute; background: var(--art-fill); border-radius: 10px; opacity: .7; }

  .title {
    position: absolute; left: 0; width: 849px; top: 28px; text-align: center;
    font-family: "Oswald", sans-serif; font-weight: 700; font-size: 85px; line-height: 1;
    color: var(--ink);
  }
  .title-sub {
    position: absolute; left: 0; width: 849px; top: 118px; text-align: center;
    font-family: "Oswald", sans-serif; font-weight: 400; font-size: 33px; line-height: 1;
    color: var(--blue); letter-spacing: 6.5px; padding-left: 6px;
  }
  .lead {
    position: absolute; left: 0; width: 849px; top: 195px; text-align: center;
    font-family: "Oswald", sans-serif; font-weight: 600; font-size: 25px; line-height: 1;
    color: var(--ink); white-space: nowrap;
  }
  .lead em { font-style: normal; color: var(--blue); }
  .banner {
    position: absolute; left: 48px; top: 247px; width: 652px; height: 56px;
    background: var(--blue); clip-path: polygon(0 0, 100% 0, 94% 100%, 5% 100%);
  }
  .banner-text {
    position: absolute; left: 76px; top: 258px;
    font-size: 28.5px; font-weight: 500; color: var(--white); line-height: 1; white-space: nowrap;
  }
  .connector { position: absolute; left: 0; top: 0; }
  .intro {
    position: absolute; left: 182px; top: 325px; width: 660px;
    font-size: 19.5px; font-weight: 600; line-height: 25px; color: var(--ink); white-space: nowrap;
  }
  .intro strong { color: var(--blue); font-weight: 700; }

  .value {
    position: absolute; font-size: 15.2px; line-height: 19.4px; text-align: justify;
    color: var(--ink);
  }
  .value strong { color: var(--blue); font-weight: 600; }
  .value-name {
    float: left; height: 48px; margin-top: -10px; margin-right: 12px;
    font-family: "Oswald", sans-serif; font-weight: 400; font-size: 36px; line-height: 1;
    color: var(--blue);
  }
  .value--family { left: 66px; top: 418px; width: 517px; }
  .value--family .value-name { margin-left: -21px; }
  .value--excellence { left: 263px; top: 564px; width: 510px; }
  .value--excellence .value-name { margin-left: -23px; }
  .value--integrity { left: 74px; top: 730px; width: 509px; }
  .value--integrity .value-name { margin-left: -26px; }
  .value--service { left: 267px; top: 881px; width: 510px; }
  .value--service .value-name { margin-left: -26px; }

  .education-badge {
    position: absolute; left: 102px; top: 997px; width: 194px; height: 194px;
    border-radius: 50%; background: var(--orange);
    display: flex; align-items: center; justify-content: center;
  }
  .education-badge p {
    transform: rotate(-16deg);
    font-family: "Oswald", sans-serif; font-weight: 400; font-size: 27px; line-height: 30px;
    color: var(--white); text-align: center;
  }
  .brand {
    position: absolute; left: 640px; top: 1040px; width: 170px;
    display: flex; flex-direction: column; align-items: center; gap: 10px;
  }
  .brand-dot { width: 22px; height: 22px; border-radius: 50%; background: var(--blue); }
  .brand-name {
    font-family: "Raleway", sans-serif; font-weight: 700; font-size: 22px; line-height: 1.1;
    color: var(--ink); text-align: center;
  }
</style>
</head>
<body>
<main class="poster">
  <svg class="backdrop" width="849" height="1200" viewBox="0 0 849 1200" aria-hidden="true">
    <circle cx="564" cy="207" r="290" fill="var(--blue-soft)"/>
    <circle cx="15" cy="495" r="170" fill="var(--blue-soft)"/>
    <circle cx="551" cy="990" r="260" fill="var(--grey-shape)"/>
    <path d="M0 1030 C60 1030 90 1080 150 1080 C230 1080 240 1040 320 1040 C400 1040 420 1110 500 1110 L849 1110 L849 1200 L0 1200 Z" fill="var(--grey-shape)"/>
  </svg>

  <span class="numeral numeral--one" aria-hidden="true">1</span>
  <span class="numeral numeral--two" aria-hidden="true">2</span>
  <span class="numeral numeral--three" aria-hidden="true">3</span>
  <span class="numeral numeral--four" aria-hidden="true">4</span>

  <div class="anatomy-art" role="img" aria-label="Line drawing of a knee joint" style="left:34px;top:32px;width:77px;height:97px"></div>
  <div class="anatomy-art" role="img" aria-label="Line drawing of a back and spine" style="left:719px;top:30px;width:98px;height:92px"></div>
  <div class="anatomy-art" role="img" aria-label="Line drawing of a hip joint" style="left:0;top:309px;width:86px;height:92px"></div>
  <div class="anatomy-art" role="img" aria-label="Line drawing of vertebrae" style="left:737px;top:430px;width:75px;height:97px"></div>
  <div class="anatomy-art" role="img" aria-label="Line drawing of a foot and heel" style="left:97px;top:587px;width:82px;height:97px"></div>
  <div class="anatomy-art" role="img" aria-label="Line drawing of a knee" style="left:674px;top:722px;width:89px;height:98px"></div>
  <div class="anatomy-art" role="img" aria-label="Line drawing of a shoulder" style="left:93px;top:878px;width:78px;height:95px"></div>

  <h1 class="title">CORE VALUES</h1>
  <p class="title-sub">FROM OUR ORGANIZATION</p>
  <p class="lead">THESE <em>CORE VALUES</em> ARE THE SPIRIT OF WHO WE ARE AS A HEALTHCARE TEAM.</p>

  <div class="banner" aria-hidden="true"></div>
  <p class="banner-text">They guide our actions, unite us in purpose,</p>
  <svg class="connector" width="849" height="400" viewBox="0 0 849 400" aria-hidden="true">
    <path d="M672 268 C710 262 738 272 716 290 C690 305 400 305 175 312 C150 318 156 332 174 338"
          fill="none" stroke="var(--ink)" stroke-width="1.5" stroke-dasharray="9 6"/>
  </svg>
  <p class="intro">- and ensure that <strong>we provide world-class care</strong> while fostering a<br>&nbsp;&nbsp;&nbsp;positive and supportive atmosphere within our team:</p>

  <section class="value value--family">
    <h2 class="value-name">Family:</h2>
    At the heart of our mission is the commitment to <strong>provide high-quality, affordable healthcare</strong> in a comforting and uplifting family-oriented environment. Just as our community is our extended family, <strong>every patient is a cherished member of our healthcare family</strong>. We treat each individual with the same care, compassion, and respect we would offer to our own loved ones.
  </section>

  <section class="value value--excellence">
    <h2 class="value-name">Excellence:</h2>
    In line with our goal, we aspire not only to alleviate pain but also to inspire patients to become active participants in their well-being. <strong>We believe in empowering our patients through education and compassion.</strong> Our pursuit of excellence is unwavering, driven by our dedication to continuously improve our services at every level, ensuring that our community receives nothing less than exceptional care.
  </section>

  <section class="value value--integrity">
    <h2 class="value-name">Integrity:</h2>
    In our healthcare team, ‘Integrity’ is non-negotiable. <strong>Our purpose is deeply rooted in ethics, integrity, and professional standards.</strong> We operate with the utmost integrity in every aspect of our work, adhering to the highest ethical principles. We understand that trust is the foundation of healthcare, and we are committed to maintaining the trust our community places in us.
  </section>

  <section class="value value--service">
    <h2 class="value-name">Service:</h2>
    Our vision is grounded in the belief that every person possesses the innate potential for true health. <strong>We aim to facilitate the body’s natural healing response by providing the highest level of service.</strong> Our hope for each patient extends beyond healing; we aspire to help you fulfill your life’s mission and purpose abundantly, supporting you in your journey to well-being.
  </section>

  <div class="education-badge">
    <p>We believe<br>that education<br>is a big part of<br>your success.</p>
  </div>

  <div class="brand">
    <span class="brand-dot" aria-hidden="true"></span>
    <span class="brand-name">Larkmoor Health</span>
  </div>
</main>
</body>
</html>
```